Reef Turtle Trust and Corvane Foundation are holding the first 'Stewardship with Color' contest.

I need a flyer/poster created about the art contest to post in schools across the state of Hawaii for grades K-12. We are trying to engage and inspire youth to learn more about this critically endangered species and it's important role to Hawaii's ecosystem. The art contest will be from March 27 - April 11, 2014. One winner from each grade will be selected and announced by late May. Students will create ‘The Island Reef Turtle, a gentle wonder’ through paint, drawing, collage or sculpture. Art medium can include: chalk, charcoal, clay, crayon, marker, paint, pen, pencil or watercolor. Students can register and submit original artwork at to www.reefturtletrust.example/drawcontest.
I need to have this flyer in a photoshop file with layers in tact so I can edit it for future years. It is imperative to incorporate each logo into the design (please let me know if you require different format? png vs. jpeg)

Requirements
Must have
• Both logos for foundations, convey that this is an art contest, dates of contest and how to submit artwork.

```html
<!DOCTYPE html>
<html lang="en">
<head>
<meta charset="utf-8">
<title>Stewardship with Color – Art Contest Poster</title>
<link rel="stylesheet" href="https://fonts.googleapis.com/css2?family=Arimo:wght@400;700&family=Chewy&family=Comfortaa:wght@700&display=swap">
<style>
  :root {
    --page: #ffffff;
    --navy: #0a2466;
    --ocean-dark: #0f4fb3;
    --ocean-mid: #1d7fd6;
    --ocean-light: #5cc4f2;
    --lilac: rgba(214, 120, 240, 0.75);
    --rose: rgba(200, 90, 130, 0.7);
    --sea-green: rgba(120, 200, 150, 0.6);
    --aqua: rgba(120, 230, 250, 0.7);
    --foam: rgba(255, 255, 255, 0.92);
    --yellow: #fff200;
    --white: #ffffff;
    --link: #39b4ec;
  }
  * { margin: 0; padding: 0; box-sizing: border-box; }
  html, body {
    width: 1000px; height: 1200px; overflow: hidden;
    background: var(--page);
  }
  .poster {
    position: absolute; left: 159px; top: 88px;
    width: 683px; height: 1025px;
    background: var(--page);
    overflow: hidden;
  }
  .ocean {
    position: absolute; left: 0; top: 0; width: 683px; height: 855px;
    background:
      radial-gradient(ellipse 60% 45% at 45% 55%, var(--ocean-light) 0%, var(--ocean-mid) 45%, transparent 80%),
      linear-gradient(180deg, var(--ocean-dark) 0%, var(--ocean-mid) 40%, var(--ocean-mid) 70%, var(--ocean-dark) 100%);
  }
  .artwork {
    position: absolute; left: 0; top: 262px; width: 683px; height: 470px;
    background:
      radial-gradient(circle at 36% 34%, var(--foam) 0%, rgba(255,255,255,0.6) 9%, transparent 17%),
      radial-gradient(circle at 66% 27%, var(--foam) 0%, rgba(255,255,255,0.6) 9%, transparent 17%),
      radial-gradient(circle at 68% 63%, var(--foam) 0%, rgba(255,255,255,0.6) 9%, transparent 17%),
      radial-gradient(circle at 38% 74%, var(--foam) 0%, rgba(255,255,255,0.6) 9%, transparent 17%),
      radial-gradient(circle at 20% 42%, var(--lilac) 0%, rgba(214,120,240,0.35) 18%, transparent 30%),
      radial-gradient(circle at 82% 62%, var(--rose) 0%, rgba(200,90,130,0.3) 18%, transparent 30%),
      radial-gradient(circle at 52% 26%, var(--sea-green) 0%, transparent 26%),
      radial-gradient(circle at 30% 70%, var(--aqua) 0%, transparent 26%);
  }
  .band { position: absolute; background: var(--navy); }
  .band--title {
    left: 0; top: 14px; width: 470px; height: 262px;
    clip-path: polygon(0 4%, 3% 0, 40% 3%, 70% 0, 100% 2%, 98% 30%, 100% 52%, 96% 60%, 60% 64%, 30% 68%, 24% 100%, 4% 97%, 0 100%);
  }
  .band--title-right {
    left: 430px; top: 60px; width: 70px; height: 105px;
    clip-path: polygon(0 0, 90% 10%, 100% 60%, 80% 100%, 0 95%);
  }
  .band--dates {
    left: 212px; top: 220px; width: 438px; height: 56px;
    clip-path: polygon(2% 8%, 40% 0, 100% 5%, 98% 50%, 100% 95%, 60% 100%, 0 96%, 1% 50%);
  }
  .band--call {
    left: 108px; top: 728px; width: 482px; height: 110px;
    background: rgba(10, 36, 102, 0.88);
    clip-path: polygon(3% 4%, 55% 0, 97% 6%, 100% 40%, 96% 70%, 86% 74%, 80% 100%, 18% 98%, 16% 72%, 2% 68%, 0 35%);
  }
  .title {
    position: absolute; left: 24px; top: 44px;
    font-family: "Comfortaa", sans-serif; font-weight: 700;
    color: var(--white); font-size: 74px; line-height: 60px;
    letter-spacing: -3px;
  }
  .title span { display: block; }
  .contest-tag {
    position: absolute; left: 322px; top: 166px;
    font-family: "Chewy", sans-serif; color: var(--yellow);
    font-size: 40px; letter-spacing: 0.5px; white-space: nowrap;
    transform: rotate(-6deg); transform-origin: left bottom;
  }
  .dates {
    position: absolute; left: 226px; top: 224px;
    font-family: "Comfortaa", sans-serif; font-weight: 700;
    color: var(--white); font-size: 37px; letter-spacing: -1px;
    white-space: nowrap;
  }
  .call {
    position: absolute; left: 90px; top: 744px; width: 520px;
    text-align: center;
    font-family: "Arimo", sans-serif; font-size: 24px; line-height: 29px;
    color: var(--white);
  }
  .call strong { color: var(--yellow); }
  .call .lead { color: var(--yellow); }
  .details {
    position: absolute; left: 0; top: 855px; width: 683px; height: 72px;
    background: var(--navy);
    font-family: "Arimo", sans-serif; font-size: 14.5px; line-height: 24px;
    color: var(--white); text-align: center; padding-top: 12px;
  }
  .details strong { font-weight: 700; }
  .details .url { color: var(--link); font-weight: 700; }
  .partners {
    position: absolute; left: 0; top: 927px; width: 683px; height: 98px;
    background: var(--page);
    display: flex; align-items: center; justify-content: space-between;
    padding: 0 48px 0 38px;
    font-family: "Arimo", sans-serif; font-weight: 700; color: var(--navy);
  }
  .partner { display: flex; align-items: center; gap: 10px; }
  .partner--corvane { font-size: 30px; letter-spacing: 1.5px; }
  .partner--reef { font-size: 18px; line-height: 20px; text-align: center; }
  .partner-mark { width: 22px; height: 22px; background: var(--navy); }
</style>
</head>
<body>
  <main class="poster">
    <div class="ocean" role="img" aria-label="Underwater ocean background in deep and bright blues"></div>
    <div class="artwork" role="img" aria-label="Illustration of four white reef turtles swimming in a circle over lilac, green, aqua and rose ripple rings"></div>

    <div class="band band--title"></div>
    <div class="band band--title-right"></div>
    <h1 class="title"><span>Stewardship</span><span>with</span><span>Color</span></h1>
    <p class="contest-tag">ART CONTEST</p>
    <div class="band band--dates"></div>
    <p class="dates">March 27 · April 11, 2014</p>

    <div class="band band--call"></div>
    <p class="call"><span class="lead">Create </span><strong>‘The Island Reef Turtle, a<br>gentle wonder’</strong> through paint, drawing,<br>collage or sculpture.</p>

    <section class="details">
      <p>Art medium can include: <strong>chalk, charcoal, clay, crayon, marker, paint, pen, pencil or watercolor.</strong></p>
      <p>Register and submit original artwork at to <span class="url">www.reefturtletrust.example/drawcontest</span></p>
    </section>

    <footer class="partners">
      <div class="partner partner--corvane">CORVANE FOUNDATION</div>
      <div class="partner partner--reef"><span class="partner-mark"></span><span>REEF TURTLE<br>TRUST</span></div>
    </footer>
  </main>
</body>
</html>
```